Plumbing business looking for a website update / to stand out

Looking to update the website with WordPress so looking for a WordPress template customised to our needs. The current website is http://www.corwinhaleplumbing.com.au/ and would like to keep the colour scheme of the green and grey. Like the idea of have menu across the top with drop down menus once mouse is over them.

Looking to stand out and look professional when compared to the competition
http://www.redgroveplumbing.net.au/
http://www.tovisplumbing.com.au/

```html
<!DOCTYPE html>
<html lang="en">
<head>
<meta charset="utf-8">
<title>Corwin Hale Plumbing</title>
<link href="https://fonts.googleapis.com/css2?family=Open+Sans:wght@400;600&family=Oswald:wght@400&display=swap" rel="stylesheet">
<style>
:root{
  --green:#5d9130;
  --green-bright:#7cc242;
  --green-dark:#3f7a1c;
  --grey-text:#6b6b6b;
  --grey-dark:#3a3a3a;
  --panel:#2f2f2f;
  --field:#e8e8e8;
  --footer:#2a2a2a;
  --sky-a:#b9d3dc;
  --sky-b:#8fb6c2;
}
*{margin:0;padding:0;box-sizing:border-box}
html,body{width:929px;height:1200px;overflow:hidden}
body{font-family:"Open Sans",Arial,sans-serif;position:relative;
  background:linear-gradient(180deg,var(--sky-a) 0%,#cfe0e6 45%,var(--sky-b) 100%)}
.page{position:absolute;left:79px;top:38px;width:774px;height:1094px;background:#fff}
.abs{position:absolute}
.brand{left:90px;top:70px;display:flex;align-items:center;gap:8px}
.brand-mark{width:26px;height:26px;border-radius:50%;background:var(--green-bright)}
.brand-name{font-size:17px;font-weight:600;color:var(--grey-dark);letter-spacing:-.3px}
.brand-tag{left:90px;top:142px;font-size:9.5px;color:var(--grey-text)}
.call{left:634px;top:71px;font-size:16px;color:var(--grey-dark)}
.call span{font-size:14px}
.badge-247{left:802px;top:61px;width:40px;height:40px;background:var(--green-bright);border-radius:3px;box-shadow:0 1px 2px rgba(0,0,0,.3)}
.nav{left:386px;top:118px;display:flex;height:39px;align-items:center;font-size:13px;color:var(--grey-dark)}
.nav a{color:inherit;text-decoration:none;padding:0 13px;line-height:39px}
.nav a.active{background:var(--green-bright);color:#fff;font-weight:600;padding:0 15px}
.hero{left:90px;top:167px;width:752px;height:311px;
  background:linear-gradient(90deg,#c9c7c2 0%,#e9e8e4 40%,#d7d5d0 70%,#a8a39a 100%)}
.callback{left:612px;top:180px;width:191px;height:284px;background:rgba(40,40,40,.92)}
.callback h3{position:absolute;left:0;top:12px;width:100%;text-align:center;font-family:"Oswald",sans-serif;font-weight:400;font-size:15px;color:#fff}
.callback h3 em{font-style:normal;color:var(--green-bright)}
.field{position:absolute;left:14px;width:163px;height:29px;background:var(--field);font-size:9px;color:#888;padding:9px 9px}
.field b{color:#222}
.submit{position:absolute;left:60px;top:235px;width:73px;height:28px;background:var(--green-bright);color:#fff;font-size:10px;display:flex;align-items:center;justify-content:center;gap:5px}
.dots{left:442px;top:490px;display:flex;gap:10px}
.dots i{width:8px;height:8px;border-radius:50%;background:#888}
.dots i:first-child{background:var(--green-bright)}
.welcome{left:90px;top:536px;font-size:16px;color:#222;font-weight:400}
.welcome em{font-style:normal;color:var(--green)}
.intro{left:90px;top:574px;width:522px;font-size:11.4px;line-height:14.7px;color:var(--grey-text);text-align:justify}
.intro p+p{margin-top:14.7px}
.services{left:636px;top:541px;width:205px;height:206px;background:var(--green);list-style:none}
.services li{height:37px;line-height:37px;color:#fff;font-size:12.5px;padding-left:28px;position:relative}
.services li::before{content:"";position:absolute;left:10px;top:16px;width:6px;height:6px;border-radius:50%;background:#fff}
.services li.on{background:var(--green-bright)}
.partner{left:90px;top:816px;width:226px;height:316px;border:1px solid #ddd;border-bottom:none}
.partner-seal{position:absolute;left:48px;top:68px;width:130px;height:130px;border-radius:50%;border:6px solid var(--green-bright)}
.partner-name{position:absolute;left:0;top:210px;width:100%;text-align:center;font-size:22px;font-weight:600;color:var(--green)}
.map{left:316px;top:816px;width:526px;height:316px;background:linear-gradient(135deg,#e6e2d6 0%,#ece9df 50%,#dedacd 100%)}
.contact{left:551px;top:827px;width:199px;height:283px;background:#f7f7f7;padding:0 0 0 32px}
.contact h4{margin-top:56px;font-family:"Oswald",sans-serif;font-weight:400;font-size:15px;color:var(--grey-dark)}
.contact h4 em{font-style:normal;color:var(--green)}
.contact p{font-size:11px;line-height:17px;color:var(--grey-text);margin-top:12px}
.footer{left:0;top:1132px;width:929px;height:68px;background:var(--footer)}
.footer-links{position:absolute;left:77px;top:15px;font-size:11px;color:#ccc}
.copy{position:absolute;left:77px;top:36px;font-size:11px;color:#aaa}
.social{position:absolute;left:739px;top:24px;display:flex;gap:11px}
.social i{width:20px;height:20px;border-radius:50%;background:#777}
</style>
</head>
<body>
<div class="page"></div>

<div class="abs brand"><span class="brand-mark"></span><span class="brand-name">Corwin Hale Plumbing</span></div>
<div class="abs brand-tag">increasing energy efficiency by design</div>
<div class="abs call">Call us <span>- 028 - 47 - 5106</span></div>
<div class="abs badge-247" aria-hidden="true">
  <svg width="40" height="40" viewBox="0 0 40 40"><circle cx="20" cy="20" r="10" fill="none" stroke="#fff" stroke-width="2"/><path d="M20 14v6l4 3" stroke="#fff" stroke-width="2" fill="none"/></svg>
</div>
<nav class="abs nav"><a class="active">Home</a><a>About Us</a><a>Services</a><a>Warrenty Agent</a><a>Team</a><a>Contact</a></nav>

<div class="abs hero" role="img" aria-label="Photo of a plumber in a blue cap fixing pipes under a kitchen sink"></div>
<form class="abs callback">
  <h3>Request a <em>Callback</em></h3>
  <div class="field" style="top:41px"><b>Name</b> (required)</div>
  <div class="field" style="top:80px"><b>Email</b> (required)</div>
  <div class="field" style="top:118px"><b>Phone</b> (required)</div>
  <div class="field" style="top:164px;height:56px"><b>Your comment</b> (required)</div>
  <div class="submit"><svg width="12" height="12" viewBox="0 0 12 12"><circle cx="6" cy="6" r="5" fill="none" stroke="#fff" stroke-width="1.3"/><path d="M4 6h4M6 4l2 2-2 2" stroke="#fff" stroke-width="1.3" fill="none"/></svg>Submit</div>
</form>
<div class="abs dots"><i></i><i></i><i></i></div>

<h2 class="abs welcome">Welcome to <em>Corwin Hale plumbing</em></h2>
<div class="abs intro">
  <p>Corwin Hale Plumbing Pty Ltd was established in 1986 and is known for high quality service that employs 5 qualified plumbing tradesmen, a Carpenter and a Sub Contractor working primarily in the Commercial and Industrial Sectors of Plumbing and Maintenance.As a locally owned Western Australian Industrial /Commercial/Maintenance Plumbing Company, we are committed to providing the best practice that will keep us as a leader in the competitive and challenging market of providing unique customer service to our clientele base.Committed to training we currently have 2 apprentice learning the trade under our direction to ensure our clientele have only the most up to date skills and techniques made available to each task at hand.</p>
  <p>We are members of The Guild of Plumbing and Gas Trades and ensure work is carried out under the regulations of the 'Plumbers Licensing Board' using the Australian Standard AS3500 bylaws, contractors license number PL 2418.Thank you for visiting our website please check out each division for a more specific understanding of our services.</p>
</div>
<ul class="abs services">
  <li>Commercial Maintanance</li>
  <li class="on">Commercial Plumbing</li>
  <li>Green Products</li>
  <li>Leak Detection Service</li>
  <li>Building and Constructions</li>
</ul>

<div class="abs partner">
  <div class="partner-seal"></div>
  <div class="partner-name">Greenway West</div>
</div>
<div class="abs map" role="img" aria-label="Street map with a location pin marking the office"></div>
<div class="abs contact">
  <h4><em>Contact</em> info</h4>
  <p>14 Harlow Lane<br>Dunmore, WA 6104<br>Australia</p>
  <p>Phone: (08) 9412 3370<br>Fax: (08) 9412 3371<br>Email: office@corwinhale.example<br>Web: corwinhale.example</p>
</div>

<footer class="abs footer">
  <div class="footer-links">Home | Before &amp; After | Home Shows | Financing | Directions | About Us | Warranty | FAQ | Contact Us | Employment</div>
  <div class="copy">Copyright © 2014 Corwin Hale plumbing , All Rights Reserved.</div>
  <div class="social"><i></i><i></i><i></i><i></i></div>
</footer>
</body>
</html>
```